We need a refreshed business card. Our company is a venture capital investment firm focused on investing in medical devices. Logo is attached. please also see our website www.velmoracapital.example

Target Market(s)

investors and potential investment targets

Industry/Entity Type

medical investments

Contact Information for Business Card

logo, name, title, email, phone, website, address,

Colors
0054AA
0677BA
7BADD7
CADEEF
E8F1F8
0094D4
00A9DD
6FCCEA
C7EBF8
E9F6FB
00AB8E
00BBA5
67D7C9
C6EFE9
E9F9F6

Requirements
Must have
• fresh modern design
Nice to have
• QR code leading to our linked in page, short description of what we do “Early Stage Medical Device Investors”

```html
<!DOCTYPE html>
<html lang="en">
<head>
<meta charset="utf-8">
<title>Velmora Business Card</title>
<link href="https://fonts.googleapis.com/css2?family=Lato:wght@400;700;900&display=swap" rel="stylesheet">
<style>
  :root {
    --brand-blue: #0054AA;
    --brand-blue-mid: #0677BA;
    --brand-blue-light: #0094D4;
    --brand-teal: #00AB8E;
    --ink-grey: #6b6f75;
    --ink-dark: #3a3d42;
    --card-white: #ffffff;
    --canvas-bg: #eceef1;
    --rule-light: rgba(255,255,255,0.7);
  }
  * { box-sizing: border-box; margin: 0; padding: 0; }
  html, body {
    width: 1200px; height: 900px; overflow: hidden;
    background: var(--canvas-bg);
    font-family: 'Lato', Arial, sans-serif;
  }
  .canvas { position: relative; width: 1200px; height: 900px; }
  .card {
    position: absolute; left: 250px; width: 700px; height: 400px;
    border-radius: 4px; box-shadow: 0 10px 30px rgba(0,0,0,0.15);
    overflow: hidden;
  }
  .card-front { top: 40px; background: var(--card-white); }
  .card-back {
    top: 470px;
    background: linear-gradient(160deg, var(--brand-blue-mid) 0%, var(--brand-blue) 100%);
  }
  .wordmark {
    position: absolute; top: 56px; left: 0; right: 0; text-align: center;
    font-weight: 900; font-size: 58px; color: var(--brand-blue); letter-spacing: 1px;
  }
  .identity { position: absolute; left: 60px; top: 205px; }
  .person-name { font-weight: 900; font-size: 30px; color: var(--brand-blue); }
  .person-title { font-size: 20px; color: var(--ink-grey); margin-top: 2px; letter-spacing: 0.5px; }
  .address { position: absolute; left: 60px; top: 300px; display: flex; gap: 12px; }
  .address-lines { font-size: 19px; color: var(--ink-dark); line-height: 1.25; letter-spacing: 0.5px; }
  .contact-list { position: absolute; left: 380px; top: 195px; list-style: none; }
  .contact-item {
    display: flex; align-items: center; gap: 12px;
    font-size: 18px; color: var(--ink-dark); line-height: 1.5; letter-spacing: 0.5px;
  }
  .icon { width: 18px; height: 18px; flex: none; }
  .back-lockup {
    position: absolute; top: 50%; left: 50%; transform: translate(-50%, -50%);
    display: flex; align-items: center; gap: 28px;
  }
  .back-wordmark { font-weight: 900; font-size: 72px; color: var(--card-white); letter-spacing: 1px; }
  .back-rule { width: 1px; height: 110px; background: var(--rule-light); }
  .back-tagline {
    font-size: 20px; color: var(--card-white); line-height: 1.15;
    letter-spacing: 2px; text-transform: uppercase;
  }
</style>
</head>
<body>
<main class="canvas">
  <section class="card card-front" aria-label="Business card front">
    <div class="wordmark">Velmora</div>
    <div class="identity">
      <h1 class="person-name">Daniel Mercer</h1>
      <p class="person-title">Principal Account Executive</p>
    </div>
    <div class="address">
      <svg class="icon" viewBox="0 0 24 24" aria-hidden="true"><path fill="var(--brand-blue)" d="M12 2a7 7 0 0 0-7 7c0 5 7 13 7 13s7-8 7-13a7 7 0 0 0-7-7zm0 9.5A2.5 2.5 0 1 1 12 6.5a2.5 2.5 0 0 1 0 5z"/></svg>
      <p class="address-lines">Harbor Lane Suite 210<br>Westfield, CA 90000</p>
    </div>
    <ul class="contact-list">
      <li class="contact-item">
        <svg class="icon" viewBox="0 0 24 24" aria-hidden="true"><path fill="var(--brand-blue)" d="M6.6 10.8a15 15 0 0 0 6.6 6.6l2.2-2.2a1 1 0 0 1 1-.25 11.4 11.4 0 0 0 3.6.57 1 1 0 0 1 1 1V20a1 1 0 0 1-1 1A17 17 0 0 1 3 4a1 1 0 0 1 1-1h3.5a1 1 0 0 1 1 1c0 1.25.2 2.45.57 3.57a1 1 0 0 1-.25 1z"/></svg>
        555.210.4836
      </li>
      <li class="contact-item">
        <svg class="icon" viewBox="0 0 24 24" aria-hidden="true"><path fill="var(--brand-blue)" d="M6 3h12v5H6zM4 9h16a2 2 0 0 1 2 2v6h-4v4H6v-4H2v-6a2 2 0 0 1 2-2zm4 7v3h8v-3z"/></svg>
        555.210.4837
      </li>
      <li class="contact-item">
        <svg class="icon" viewBox="0 0 24 24" aria-hidden="true"><path fill="var(--brand-blue)" d="M2 5h20v14H2zm2 2v.5l8 5 8-5V7l-8 5z"/></svg>
        hello@velmoracapital.example
      </li>
      <li class="contact-item">
        <svg class="icon" viewBox="0 0 24 24" aria-hidden="true"><g fill="none" stroke="var(--brand-blue)" stroke-width="2"><circle cx="12" cy="12" r="9"/><path d="M3 12h18M12 3c3 3 3 15 0 18M12 3c-3 3-3 15 0 18"/></g></svg>
        www.velmoracapital.example
      </li>
    </ul>
  </section>

  <section class="card card-back" aria-label="Business card back">
    <div class="back-lockup">
      <div class="back-wordmark">Velmora</div>
      <div class="back-rule"></div>
      <p class="back-tagline">Medical<br>Device<br>Ventures</p>
    </div>
  </section>
</main>
</body>
</html>
```